Xmas Greeting for Email for Corvath Solutions

We would love to have a beautifully designed Xmas card that we can send to our clients .
The card will be used to thank our clients for their support during the year and to wish them a Merry Xmas and a Good New year (2020).

We would like a design that is simple and very elegant.

Target Market(s)

Our clients

Font styles to use
Script

Colors

Designer to choose colors to be used in the design.

Requirements
Must have
• 1. Our logo (see attached)
• 2. A message that thanks our clients for their support during the year.
• 3. the message "Merry Christmas & Happy New Year"
• 4. Design must be simple and elegant

```html
<!DOCTYPE html>
<html lang="en">
<head>
<meta charset="utf-8">
<title>Corvath Solutions – Christmas Greeting</title>
<link href="https://fonts.googleapis.com/css2?family=Amatic+SC:wght@700&display=swap" rel="stylesheet">
<style>
  :root {
    --page: #ffffff;
    --navy-deep: #16295a;
    --navy: #234a8a;
    --navy-glow: #3a63a6;
    --ink-light: #ffffff;
    --ornament-red: #e2404a;
    --ornament-cyan: #3fbfe0;
    --ornament-purple: #a04aa8;
    --ornament-lime: #c6d82a;
    --ornament-orange: #f29a2e;
  }
  * { margin: 0; padding: 0; box-sizing: border-box; }
  html, body { width: 1200px; height: 763px; overflow: hidden; background: var(--page); }
  .canvas { position: relative; width: 1200px; height: 763px; background: var(--page); }

  .card {
    position: absolute;
    top: 40px;
    width: 489px;
    height: 684px;
    overflow: hidden;
    background:
      radial-gradient(ellipse at 50% 45%, var(--navy-glow) 0%, var(--navy) 45%, var(--navy-deep) 100%);
    font-family: "Amatic SC", "Arial Narrow", sans-serif;
    font-weight: 700;
    color: var(--ink-light);
    text-align: center;
  }
  .card--front { left: 69px; }
  .card--back { left: 631px; }

  .brand {
    position: absolute;
    display: flex;
    align-items: center;
    gap: 14px;
    white-space: nowrap;
    letter-spacing: 2px;
    color: var(--ink-light);
  }
  .brand__dot {
    display: block;
    border-radius: 50%;
    background: var(--ink-light);
    opacity: 0.9;
  }
  .card--front .brand { left: 84px; top: 46px; font-size: 34px; }
  .card--front .brand__dot { width: 52px; height: 52px; }
  .card--back .brand { left: 80px; top: 546px; font-size: 36px; }
  .card--back .brand__dot { width: 84px; height: 84px; }

  .tree-art {
    position: absolute;
    left: 60px;
    top: 112px;
    width: 372px;
    height: 448px;
    clip-path: polygon(50% 0, 100% 100%, 0 100%);
    background:
      radial-gradient(circle at 50% 60%, rgba(198,216,42,0.55) 0%, rgba(63,191,224,0.45) 35%, rgba(160,74,168,0.45) 60%, rgba(226,64,74,0.5) 85%);
  }

  .greeting-front {
    position: absolute;
    left: 0;
    right: 0;
    top: 576px;
    font-size: 40px;
    line-height: 44px;
    letter-spacing: 4px;
  }

  .ornaments-art {
    position: absolute;
    left: 110px;
    top: 0;
    width: 278px;
    height: 150px;
    background:
      linear-gradient(90deg, rgba(226,64,74,0.55), rgba(63,191,224,0.55), rgba(160,74,168,0.55), rgba(198,216,42,0.55), rgba(242,154,46,0.55));
    border-radius: 0 0 60px 60px;
  }

  .message {
    position: absolute;
    left: 0;
    right: 0;
    font-size: 38px;
    line-height: 36px;
    letter-spacing: 3px;
  }
  .message--wish { top: 232px; }
  .message--thanks { top: 378px; }
</style>
</head>
<body>
<main class="canvas">

  <section class="card card--front" aria-label="Card front">
    <div class="brand">
      <span class="brand__dot" aria-hidden="true"></span>
      <span class="brand__name">Corvath Solutions</span>
    </div>
    <div class="tree-art" role="img" aria-label="Christmas tree built from colourful baubles wrapped in a white ribbon, topped with an orange star"></div>
    <p class="greeting-front">Merry Christmas<br>&amp; Happy New Year</p>
  </section>

  <section class="card card--back" aria-label="Card back">
    <div class="ornaments-art" role="img" aria-label="Five colourful baubles hanging on white strings"></div>
    <p class="message message--wish">Merry Christmas<br>and a successful<br>2020 from our team.</p>
    <p class="message message--thanks">Thank you for the<br>partnership in the<br>past year.</p>
    <div class="brand">
      <span class="brand__dot" aria-hidden="true"></span>
      <span class="brand__name">Corvath Solutions</span>
    </div>
  </section>

</main>
</body>
</html>
```